I need a OptiDisc cover for a training package contained on a disc. There are four modules within the resource so I need these to be visible on the cover. They are:
Cultural Competence Healthcare Provision
Provision of Care to CALD Women having Babies in Australia
Cultural Considerations in Aged Care Provision
Cultural Competence in Mental Health

I have attached a cd cover with an image of a waratah. This is Corrowin Basin Health's logo so needs to appear on the front cover also.
The smaller logo with the waratah also needs to be on the front cover. Please note these are the only copies I could obtain so if the quality is too poor you may need to reproduce.

The following should appear on the back cover:
‘Pathways Beyond the Bedside’ is a collaborative achievement of the Multicultural Health Liaison Officers in Acute Care, Obstetrics, Aged Care and Mental Health under the guidance of the Director, Multicultural Health Service in Corrowin Basin Local Health District. Staff members from the specialist teams and community members graciously contributed to the production of podcasts and video clips.
Photography, video clips and technical support was provided by Gordon Velasky - E-learning Developer and Designer - Lumen Tutorworks.
This project was coordinated by Colette Brandt, Multicultural Health Liaison Officer (Acute Care, Tallowmere Ridge Clinical Hospital Network).

```html
<!DOCTYPE html>
<html lang="en">
<head>
<meta charset="utf-8">
<title>Pathways Beyond the Bedside – Disc Cover</title>
<link rel="stylesheet" href="https://fonts.googleapis.com/css2?family=Arimo:wght@400;700&family=Comic+Neue:wght@400;700&display=swap">
<style>
:root{
  --frame:#050505;
  --sleeve:#f0c283;
  --navy:#1c1a66;
  --title-red:#d23a3a;
  --heading-blue:#1b78c2;
  --ink:#111111;
  --spine-text:#ffffff;
  --photo-warm:#c9a07a;
  --photo-sand:#a58260;
  --logo-red:#d8262b;
}
*{margin:0;padding:0;box-sizing:border-box}
html,body{width:1200px;height:1000px;overflow:hidden;background:var(--frame)}
.cover{position:relative;width:1200px;height:1000px;background:var(--frame);font-family:"Arimo",Arial,sans-serif}
.panel{position:absolute;top:5px;bottom:5px;background:var(--sleeve)}
.back{left:5px;width:565px}
.front{left:631px;width:564px}
.spine{position:absolute;left:570px;top:0;width:61px;height:1000px;background:var(--frame)}
.spine-title{position:absolute;left:50%;top:70px;transform:translateX(-50%);
  writing-mode:vertical-rl;text-orientation:upright;color:var(--spine-text);
  font-size:18px;letter-spacing:8.6px;line-height:1}
.photo{position:absolute}
.photo-care{left:23px;top:21px;width:172px;height:112px;border:2px solid #8e8e8e;
  background:linear-gradient(135deg,#e9e6e0 0%,#d7b79a 45%,#6b4a3a 75%,#f2f2f2 100%)}
.photo-hands{left:278px;top:837px;width:265px;height:140px;border:4px solid #3a2f2a;border-radius:3px;
  background:radial-gradient(ellipse at center,var(--photo-warm) 0%,var(--photo-sand) 45%,#4a3428 100%)}
.back-copy{position:absolute;left:14px;top:150px;width:545px;color:var(--navy);font-size:20px;line-height:46px}
.back-copy p+p{margin-top:46px}
.title{position:absolute;font-family:"Comic Neue","Comic Sans MS",cursive;color:var(--title-red);font-size:45px;font-weight:400;line-height:1}
.title-l1{left:14px;top:128px}
.title-l2{left:90px;top:192px}
.modules{position:absolute;left:0;top:378px;width:100%;text-align:center}
.modules-heading{color:var(--heading-blue);font-size:26px;text-decoration:underline;text-underline-offset:4px;font-weight:400}
.module-list{list-style:none;margin-top:22px;color:var(--ink);font-size:21px}
.module-list li{height:57.5px}
.brand{position:absolute;left:0;top:800px;width:100%;display:flex;justify-content:center;align-items:center;gap:12px}
.brand-dot{width:22px;height:22px;border-radius:50%;background:var(--logo-red)}
.brand-name{font-size:26px;font-weight:700;color:var(--logo-red)}
.format-mark{position:absolute;left:40px;top:925px;font-size:22px;font-weight:700;color:var(--ink)}
</style>
</head>
<body>
<main class="cover">
  <section class="panel back">
    <div class="photo photo-care" role="img" aria-label="Photo of a nurse checking a baby held by its mother"></div>
    <div class="back-copy">
      <p>‘Pathways Beyond the Bedside’ is a collaborative achievement of the Multicultural Health Liaison Officers in Acute Care, Obstetrics, Aged Care and Mental Health under the guidance of the Director, Multicultural Health Service in Corrowin Basin Local Health District. Staff members from the specialist teams and community members graciously contributed to the production of podcasts and video clips.</p>
      <p>Photography, video clips and technical support was provided by Gordon Velasky - E-learning Developer and Designer - Lumen Tutorworks.</p>
      <p>This project was coordinated by Colette Brandt, Multicultural Health Liaison Officer (Acute Care, Tallowmere Ridge Clinical Hospital Network).</p>
    </div>
    <div class="photo photo-hands" role="img" aria-label="Photo of many hands reaching into a circle of sand"></div>
  </section>

  <aside class="spine">
    <span class="spine-title">Pathways Beyond the Bedside</span>
  </aside>

  <section class="panel front">
    <h1 class="title title-l1">Pathways Beyond</h1>
    <h1 class="title title-l2">the Bedside</h1>
    <div class="modules">
      <h2 class="modules-heading">There are four modules within the resource</h2>
      <ul class="module-list">
        <li>Cultural Competence Healthcare Provision</li>
        <li>Provision of Care to CALD Women having Babies in Australia</li>
        <li>Cultural Considerations in Aged Care Provision</li>
        <li>Cultural Competence in Mental Health</li>
      </ul>
    </div>
    <div class="brand">
      <span class="brand-dot"></span>
      <span class="brand-name">Corrowin Basin Health</span>
    </div>
    <span class="format-mark">OptiDisc</span>
  </section>
</main>
</body>
</html>
```